Website R86 coffee

I am opening a small business selling locally roasted coffee online. To start with I want a site with three pages. 1. A welcome page with logo and mission/vision. 2. Shopping/ordering page. 3. About Us page. The brand is "R86 Coffee - A warm start to every day". We are giving back to the downs syndrome community by employing people with down syndrome (Trisomy 21) and buy donating to down syndrome research.

Target Market(s)

Families and friends of people with downs syndrome

Coding

Coded - Design and coding required

Number of Pages Required

3 page

```html
<!DOCTYPE html>
<html lang="en">
<head>
<meta charset="utf-8">
<title>R86 Coffee</title>
<link rel="stylesheet" href="https://fonts.googleapis.com/css2?family=Montserrat:wght@600&family=Space+Grotesk:wght@300;400&display=swap">
<style>
:root{
  --ink:#111;
  --text:#333;
  --muted:#555;
  --rule:#ddd;
  --footer:#efefef;
  --field:#dcdcdc;
  --white:#fff;
  --hero-a:#2a2520;
  --hero-b:#5a4030;
}
*{margin:0;padding:0;box-sizing:border-box}
html,body{width:961px;height:1200px;overflow:hidden;background:var(--white)}
body{position:relative;font-family:"Space Grotesk",sans-serif;color:var(--text)}
.abs{position:absolute}
.icon-box{width:28px;height:28px;border:1.5px solid var(--ink);display:flex;align-items:center;justify-content:center}
.top-text{font-size:12px;color:var(--text)}
.brand{display:flex;align-items:center;gap:6px;font-size:17px;font-weight:400;color:var(--ink);letter-spacing:.5px}
.brand-square{width:10px;height:10px;background:var(--ink)}
.nav-rule{left:152px;top:83px;width:656px;height:1px;background:var(--rule)}
.nav-active{left:380px;top:82px;width:32px;height:2px;background:var(--ink)}
.nav{top:97px;left:0;width:961px;display:flex;justify-content:center;gap:19px;font-size:10px;text-transform:uppercase;color:var(--ink);padding-left:20px}
.hero{left:48px;top:123px;width:864px;height:447px;background:radial-gradient(ellipse at 35% 70%,var(--hero-b),var(--hero-a) 75%)}
.hero-title{top:257px;left:0;width:961px;text-align:center;font-family:"Montserrat",sans-serif;font-weight:600;font-size:37px;line-height:45px;color:var(--white)}
.hero-sub{top:355px;left:0;width:961px;text-align:center;font-size:13.5px;color:var(--white)}
.hero-btn{left:427px;top:395px;width:106px;height:33px;border:1px solid var(--white);color:var(--white);font-size:12.5px;display:flex;align-items:center;justify-content:center}
.dots{left:454px;top:549px;display:flex;gap:6px}
.dots span{width:6px;height:6px;border:1px solid #666}
.dots span.on{background:var(--white);border-color:var(--white)}
.section-title{left:0;width:961px;text-align:center;font-weight:300;font-size:25px;color:var(--ink);letter-spacing:.5px}
.section-copy{left:0;width:961px;text-align:center;font-size:10px;line-height:17px;color:var(--muted);letter-spacing:.3px}
.order-btn{left:420px;top:870px;width:120px;height:36px;background:var(--ink);color:var(--white);font-size:12px;display:flex;align-items:center;justify-content:center}
.footer{left:48px;top:970px;width:864px;height:229px;background:var(--footer)}
.footer-rule{left:48px;top:1161px;width:864px;height:1px;background:var(--rule)}
.copyright{left:0;top:1174px;width:961px;text-align:center;font-size:9px;color:var(--muted)}
.f-head{font-size:11.5px;color:var(--ink);text-transform:uppercase;top:1006px}
.sitemap{left:270px;top:1037px;list-style:none;font-size:9.5px;color:var(--muted);line-height:18px}
.sitemap li::before{content:"";display:inline-block;width:4px;height:4px;background:var(--ink);margin:0 9px 2px 0}
.social{top:1098px;display:flex;gap:6px;left:105px}
.social span{width:27px;height:27px;border:1px solid var(--ink)}
.signup-copy{left:710px;top:1031px;width:200px;font-size:9.5px;line-height:18px;color:var(--muted)}
.signup-field{left:709px;top:1077px;width:186px;height:30px;background:var(--field);font-size:9px;color:var(--muted);padding:9px 11px}
.signup-btn{left:868px;top:1080px;width:24px;height:24px;background:var(--ink);display:flex;align-items:center;justify-content:center}
</style>
</head>
<body>
<header>
  <div class="abs icon-box" style="left:48px;top:27px">
    <svg width="14" height="14" viewBox="0 0 24 24"><path d="M6.6 10.8a15 15 0 0 0 6.6 6.6l2.2-2.2c.3-.3.7-.4 1-.2 1.1.4 2.3.6 3.6.6.6 0 1 .4 1 1V20c0 .6-.4 1-1 1A17 17 0 0 1 3 4c0-.6.4-1 1-1h3.5c.6 0 1 .4 1 1 0 1.2.2 2.4.6 3.6.1.3 0 .7-.2 1z" fill="#111"/></svg>
  </div>
  <div class="abs top-text" style="left:84px;top:33px">+1 555 010 2486</div>
  <div class="abs brand" style="left:425px;top:30px"><span class="brand-square"></span>R86 Coffee</div>
  <div class="abs icon-box" style="left:749px;top:27px">
    <svg width="13" height="14" viewBox="0 0 24 24"><circle cx="12" cy="7" r="5" fill="#111"/><path d="M3 23c0-6 4-9 9-9s9 3 9 9z" fill="#111"/></svg>
  </div>
  <div class="abs top-text" style="left:783px;top:33px;font-size:10.5px">Login</div>
  <div class="abs icon-box" style="left:822px;top:27px">
    <svg width="16" height="14" viewBox="0 0 24 20" fill="none" stroke="#111" stroke-width="1.8"><path d="M1 2h4l3 11h12l2-8H7"/><circle cx="10" cy="17" r="1.5"/><circle cx="18" cy="17" r="1.5"/></svg>
  </div>
  <div class="abs top-text" style="left:852px;top:33px;font-size:10.5px">Add To Cart</div>
  <div class="abs nav-rule"></div>
  <div class="abs nav-active"></div>
  <nav class="abs nav"><span>Home</span><span>Shopping/Ordering</span><span>About Us</span></nav>
</header>

<section>
  <div class="abs hero" role="img" aria-label="Freshly roasted coffee beans pouring from a roaster drum, scooped by hand"></div>
  <h1 class="abs hero-title">ROASTED COFFEE<br>NOW ONLINE</h1>
  <p class="abs hero-sub">A Warm Start To Every Day</p>
  <div class="abs hero-btn">SHOP NOW</div>
  <div class="abs dots"><span></span><span></span><span class="on"></span><span></span><span></span></div>
</section>

<section>
  <h2 class="abs section-title" style="top:625px">VISION</h2>
  <p class="abs section-copy" style="top:666px">Develop a company that markets coffee and related products to family and<br>friends of the down syndrome community</p>
  <h2 class="abs section-title" style="top:732px">MISSION</h2>
  <p class="abs section-copy" style="top:773px">create and grow an online&nbsp; company selling contract roasted coffee. as growth permits<br>become a fully&nbsp; vertically integrated&nbsp; coffee company from roasting to our own coffee<br>shop. The company will give significant funds&nbsp; to medical research&nbsp; in downs syndrome<br>and we will hire as many people with Downs syndrome as possible.</p>
  <div class="abs order-btn">ORDER NOW</div>
</section>

<footer>
  <div class="abs footer"></div>
  <div class="abs brand" style="left:100px;top:1040px"><span class="brand-square"></span>R86 Coffee</div>
  <div class="abs social"><span></span><span></span><span></span></div>

  <div class="abs f-head" style="left:270px">Sitemap</div>
  <ul class="abs sitemap">
    <li>Home</li><li>Shopping/Ordering</li><li>About Us</li><li>Privacy Policy</li><li>Terms &amp; Conditions</li>
  </ul>

  <div class="abs f-head" style="left:490px">Contact Us</div>
  <svg class="abs" style="left:488px;top:1039px" width="15" height="15" viewBox="0 0 24 24"><path d="M6.6 10.8a15 15 0 0 0 6.6 6.6l2.2-2.2c.3-.3.7-.4 1-.2 1.1.4 2.3.6 3.6.6.6 0 1 .4 1 1V20c0 .6-.4 1-1 1A17 17 0 0 1 3 4c0-.6.4-1 1-1h3.5c.6 0 1 .4 1 1 0 1.2.2 2.4.6 3.6.1.3 0 .7-.2 1z" fill="#111"/></svg>
  <div class="abs" style="left:518px;top:1034px;font-size:9.5px;color:var(--muted)">Call Us On</div>
  <div class="abs" style="left:517px;top:1048px;font-size:12px;color:var(--text)">+1 555 010 2486</div>
  <svg class="abs" style="left:488px;top:1086px" width="15" height="12" viewBox="0 0 24 18"><rect width="24" height="18" rx="2" fill="#111"/><path d="M1 2l11 8 11-8" stroke="#efefef" stroke-width="2" fill="none"/></svg>
  <div class="abs" style="left:516px;top:1084px;font-size:12px;color:var(--text)">info@r86coffee.com</div>

  <div class="abs f-head" style="left:710px">Stay Upto Date With Us</div>
  <p class="abs signup-copy">Would you like to receive our exclusive update for signup !</p>
  <div class="abs signup-field">Enter Email *</div>
  <div class="abs signup-btn">
    <svg width="12" height="12" viewBox="0 0 24 24"><path d="M2 11l20-9-7 20-3-8z" fill="#fff"/></svg>
  </div>

  <div class="abs footer-rule"></div>
  <div class="abs copyright">©R86COFFEE - 2021 All rights reserved.</div>
</footer>
</body>
</html>
```